IT Services company requires a services website design with integrated blog

We at Brindle Harbour Systems primarily provide application migration consultancy (e.g. moving applications from Plexor OS 4 to Plexor 9) and application virtualization (e.g. Norvane StackPod) consultancy.This process is commonly known as 'packaging' but doesnt involve cardboard boxes ;) (however, I am happy to use that visual analogy if you want to use any box graphics) We also provide application compatibility testing, software auditing and application portfolio management.

We are looking for a complete redesign of our current horrible diy attempt at a website at www.example-vendorhub.test. We have had created a rebranded logo (attached files and fonts) and a rebranded business card (also attached) We would like the website to match the same/similar colors and styling as these.

I want to redisgn the website so that the main focus of this website is to show our subject matter expertise with a blog and should take up most of the websites real estate and focus on the home screen. Then if the customer wants, they can use our services to help them in their own application migration/deployment projects by browsing our details in links/buttons somewhere
Updates

In any of the designs, please do not include my Quellbright or Norvane partnerships.  Thank you

Target Market(s)

Application packagers / engineers looking for technical articles

Application migration project managers

Industry/Entity Type

Real Estate

Requirements
Must have
• This site is primarily a blog site. The blog should have buttons to share each article on social media site. It should be easy for me to create or edit new blog articles (have technical skills but not creative ones). Each article should also allow for comments (do not require approval but should allow for admin removal) but do not add like/vote buttons because i do not expect large enough traffic and could be determental.

There should be a contact page to host contact information and an email box that goes to enquiries@example-vendorhub.test

The other pages should include About us and Services (placeholder text to be used as current site text needs overhauling but original text can be used in the design just remember when placing that the text may shorten or increase etc.)

All text has to be easily editable (no over use of text in images where possible)
Nice to have
• An email notification of new comments to articles sent to webadmin@example-vendorhub.test

Newsletter subscription
Should not have
• Do not include vote/like buttons or website counters. Initial traffic is not going to be large enough to warrant these features and may reflect badly on the site.

No logon features. Site content and commenting should be open access

No opinion polls

No why choose us section from current website

Do not include partner information in new site (Quellbright and Norvane)

DO NOT JUST REPLICATE EXISTING WEBSITE FEATURES, PLEASE REFER TO THIS BRIEF. THIS SITE NEEDS TO PRIMARILY BE A BLOG

```html
<!DOCTYPE html>
<html lang="en">
<head>
<meta charset="utf-8">
<title>Brindle Harbour Systems – Blog</title>
<link href="https://fonts.googleapis.com/css2?family=PT+Sans:wght@400;700&family=Nunito:wght@700;800&display=swap" rel="stylesheet">
<style>
:root{
  --blue-deep:#1637a6;
  --blue-mid:#1f4fc4;
  --blue-light:#2f6bdc;
  --blue-text:#0d4ec4;
  --orange:#e58b1c;
  --gold:#f6b62b;
  --grey-band:#eeeeee;
  --grey-text:#6d6d6d;
  --dark:#2a2a2a;
  --white:#ffffff;
}
*{box-sizing:border-box;margin:0;padding:0}
html,body{width:1104px;height:1200px;overflow:hidden}
body{font-family:"PT Sans",sans-serif;color:var(--dark);background:var(--white);position:relative}

.site-header{position:absolute;left:0;top:0;width:1104px;height:330px;
  background:radial-gradient(ellipse 520px 300px at 420px 200px,var(--blue-light),var(--blue-mid) 55%,var(--blue-deep))}
.brand{position:absolute;left:166px;top:46px;display:flex;align-items:center;gap:10px}
.brand-dot{width:26px;height:26px;border-radius:50%;background:#dfe6f3}
.brand-name{font-size:22px;color:#dfe6f3}
.search{position:absolute;left:740px;top:24px;width:184px;height:23px;border:1px solid #0c2a8a;background:var(--blue-deep);color:#d8e2ff;font-size:11px;padding:4px 12px}
.search-icon{position:absolute;left:932px;top:27px}
.top-nav{position:absolute;right:155px;top:70px;display:flex;gap:14px;font-family:"Nunito",sans-serif;font-weight:800;font-size:11.5px;color:var(--gold);letter-spacing:.3px}
.top-nav .sep{color:#c7d3f6;font-weight:400}
.hero-visual{position:absolute;left:300px;top:104px;width:340px;height:226px;border-radius:8px 8px 0 0;
  background:linear-gradient(180deg,rgba(90,140,235,.55),rgba(40,70,160,.75))}

.quote-band{position:absolute;left:0;top:330px;width:1104px;height:72px;background:var(--grey-band)}
.quote-mark{position:absolute;top:8px;font-family:"Nunito",sans-serif;font-weight:800;font-size:62px;color:#555;line-height:1}
.quote-text{position:absolute;left:217px;top:14px;font-size:17px;color:var(--grey-text);line-height:22px}
.quote-text .source{font-family:"Nunito",sans-serif;font-weight:800;font-size:11.5px;color:var(--blue-text);margin-left:4px}
.details-btn{position:absolute;left:773px;top:18px;width:129px;height:33px;border-radius:17px;
  background:linear-gradient(#2a74e6,#0b44c0);border:2px solid #0b3aa6;color:var(--white);
  font-family:"Nunito",sans-serif;font-weight:800;font-size:12px;display:flex;align-items:center;justify-content:center;
  box-shadow:0 6px 8px -4px rgba(0,0,0,.25)}

.main-nav{position:absolute;left:0;top:402px;width:1104px;height:66px;background:var(--white)}
.main-nav a{position:absolute;top:17px;height:49px;line-height:34px;font-family:"Nunito",sans-serif;font-weight:800;font-size:11.5px;color:var(--grey-text);text-decoration:none;letter-spacing:.3px}
.main-nav a.active{background:var(--blue-mid);color:var(--white);width:138px;text-align:center}

.content{position:absolute;left:0;top:468px;width:1104px;height:675px;
  background:radial-gradient(ellipse 600px 340px at 552px 300px,var(--blue-light),var(--blue-mid) 60%,var(--blue-deep))}

.post{position:absolute;left:158px;width:791px;background:var(--white);padding:0 17px;box-shadow:0 2px 3px rgba(0,0,0,.3)}
.post-head{position:relative;height:30px}
.post-title{position:absolute;left:0;top:13px;font-family:"Nunito",sans-serif;font-weight:800;font-size:11.5px;color:var(--blue-text)}
.post-tools{position:absolute;left:492px;top:13px;display:flex;gap:9px}
.share{position:absolute;left:703px;top:13px;display:flex;height:15px;font-size:9px;border:1px solid #c9c9c9;border-radius:2px}
.share .label{display:flex;align-items:center;gap:3px;padding:0 3px;background:#f5f5f5;border-right:1px solid #c9c9c9}
.share .label i{width:10px;height:10px;background:#2f9a3a;border-radius:1px;display:block}
.share .count{padding:0 5px;line-height:13px;color:#666}
.post-date{display:inline-block;margin-left:-2px;background:var(--orange);font-size:9.5px;color:#3a2000;padding:1px 6px;height:15px;line-height:13px}
.post-date em{font-style:normal;color:var(--white)}
.post p{font-size:10.5px;line-height:14.5px;margin-top:7px}
.code-box{margin-top:12px;width:368px;border:1px dashed #a5a5a5;padding:4px 10px;font-size:11px;color:var(--blue-text);line-height:19.4px}
.read-more{display:inline-block;margin:8px 0 12px;font-size:9.5px;color:var(--dark);padding:1px 5px;background:#d4d4d4;border:1px solid #b0b0b0;text-decoration:underline}

.pager{position:absolute;left:642px;top:966px;height:29px;display:flex;border:1px solid #0a1f5f;background:var(--white);font-size:11.5px}
.pager span{display:flex;align-items:center;justify-content:center;width:27.5px;border-left:1px solid #555;color:var(--dark)}
.pager span.current{color:var(--blue-text)}
.pager .step{width:80px;background:var(--blue-mid);color:var(--white);border:none;gap:6px}
.pager .step.next{width:60px;border-left:1px solid #555}

.site-footer{position:absolute;left:0;top:1143px;width:1104px;height:57px;background:var(--white)}
.footer-links{position:absolute;left:157px;top:18px;font-size:7.5px;color:var(--blue-text);word-spacing:2px}
.copyright{position:absolute;left:157px;top:36px;font-size:7px;color:#666}
</style>
</head>
<body>

<header class="site-header">
  <div class="brand"><span class="brand-dot"></span><span class="brand-name">Brindle Harbour Systems</span></div>
  <div class="search">Search</div>
  <svg class="search-icon" width="17" height="17" viewBox="0 0 17 17" fill="none" stroke="#dfe6f3" stroke-width="1.6"><circle cx="10.5" cy="6.5" r="5"/><line x1="7" y1="10" x2="1.5" y2="15.5"/></svg>
  <nav class="top-nav">
    <span>ABOUT US</span><span class="sep">|</span>
    <span>OUR SERVICES</span><span class="sep">|</span>
    <span>CONTACT</span>
  </nav>
  <div class="hero-visual" role="img" aria-label="Photo of two business people with a laptop, one pointing at a glowing data interface"></div>
</header>

<section class="quote-band">
  <span class="quote-mark" style="left:168px">“</span>
  <p class="quote-text">Logistics- The detailed orgainization andimplementation<br>&nbsp;of a complex operation <span class="source">Harwell Lexicon</span></p>
  <span class="quote-mark" style="left:652px">”</span>
  <div class="details-btn">OUR DETAILS</div>
</section>

<nav class="main-nav">
  <a style="left:181px">HOME</a>
  <a style="left:306px">ABOUT US</a>
  <a style="left:455px">OUR SERVICES</a>
  <a class="active" style="left:634px">BLOG</a>
  <a style="left:836px">CONTACT</a>
</nav>

<main class="content"></main>

<article class="post" style="top:486px">
  <div class="post-head">
    <h2 class="post-title">How To Run Local Applications Within a StackPod 5 Sequence</h2>
    <div class="post-tools">
      <svg width="11" height="12" viewBox="0 0 11 12"><rect x="1" y="0.5" width="9" height="11" fill="#fff" stroke="#c22"/><line x1="3" y1="5" x2="8" y2="5" stroke="#c22"/><line x1="3" y1="8" x2="8" y2="8" stroke="#c22"/></svg>
      <svg width="13" height="12" viewBox="0 0 13 12"><rect x="3" y="0.5" width="7" height="4" fill="#fff" stroke="#d97a10"/><rect x="0.5" y="4" width="12" height="5" fill="#f0a030" stroke="#d97a10"/><rect x="3" y="8" width="7" height="3.5" fill="#fff" stroke="#d97a10"/></svg>
      <svg width="13" height="12" viewBox="0 0 13 12"><rect x="0.5" y="5" width="12" height="6.5" fill="#f6d070" stroke="#c9941c"/><path d="M6.5 0v5M4 3l2.5 2.5L9 3" stroke="#2f9a3a" stroke-width="1.5" fill="none"/></svg>
    </div>
    <div class="share"><span class="label"><i></i>Share</span><span class="count">3K</span></div>
  </div>
  <span class="post-date">Thursday, 08 <em>November</em> 2012 13:46</span>
  <p>Those of us that are used to StackPod before version 5 may be used to using the Podtray.exe with the /exe switch to run a command within the StackPod sequence. With StackPod 5 this has now gone. Instead StackPod 5 is Shellforge driven and there is a new cmdlet to achieve the same result. To do this you now run the following Shellforge cmdlets (this example executes scratchpad.exe within the My Application sequence):</p>
  <div class="code-box">
    Import-Module StackPodClient<br>
    $Package = Get-StackPodPackage ("My Application")<br>
    Start-StackPodProcess -StackPodObject $Package "scratchpad.exe"
  </div>
  <p style="margin-top:12px">Note that Start-StackPodProcess accepts the same parameters as the standard Start-Process cmdlet such as the ability to change window style (such as minimized), run as a different user, etc.</p>
  <a class="read-more">Read more</a>
</article>

<article class="post" style="top:760px">
  <div class="post-head">
    <h2 class="post-title">Isolating Wavepoint Browser Within StackPod</h2>
    <div class="post-tools">
      <svg width="11" height="12" viewBox="0 0 11 12"><rect x="1" y="0.5" width="9" height="11" fill="#fff" stroke="#c22"/><line x1="3" y1="5" x2="8" y2="5" stroke="#c22"/><line x1="3" y1="8" x2="8" y2="8" stroke="#c22"/></svg>
      <svg width="13" height="12" viewBox="0 0 13 12"><rect x="3" y="0.5" width="7" height="4" fill="#fff" stroke="#d97a10"/><rect x="0.5" y="4" width="12" height="5" fill="#f0a030" stroke="#d97a10"/><rect x="3" y="8" width="7" height="3.5" fill="#fff" stroke="#d97a10"/></svg>
      <svg width="13" height="12" viewBox="0 0 13 12"><rect x="0.5" y="5" width="12" height="6.5" fill="#f6d070" stroke="#c9941c"/><path d="M6.5 0v5M4 3l2.5 2.5L9 3" stroke="#2f9a3a" stroke-width="1.5" fill="none"/></svg>
    </div>
    <div class="share"><span class="label"><i></i>Share</span><span class="count">3K</span></div>
  </div>
  <span class="post-date">Thursday, 31 <em>May</em> 2012 10:25</span>
  <p>I recently came across a interesting scenario whilst sequencing Wavepoint Browser add-ons.</p>
  <p style="margin-top:14px">My scenario was this: I had an Wavepoint Browser based application that required a specific version of Cobalt Runtime. On the local PC image is a newer version of Cobalt Runtime. My sequence was to contain the specified version of Cobalt Runtime with a shortcut to the locally installed Wavepoint Browser with the website as a parameter. In theory, when launching the website from my sequenced application shortcut the older version of Cobalt Runtime should be used and not the locally installed one.</p>
  <a class="read-more" style="margin-top:14px">Read more</a>
</article>

<nav class="pager">
  <span class="step">
    <svg width="16" height="8" viewBox="0 0 16 8"><path d="M1 4h14M4 1L1 4l3 3" stroke="#fff" stroke-width="1.3" fill="none"/></svg>Previous
  </span>
  <span class="current">1</span><span>2</span><span>3</span><span>4</span><span>5</span><span>6</span>
  <span class="step next">Next
    <svg width="16" height="8" viewBox="0 0 16 8"><path d="M1 4h14M12 1l3 3-3 3" stroke="#fff" stroke-width="1.3" fill="none"/></svg>
  </span>
</nav>

<footer class="site-footer">
  <div class="footer-links">HOME &nbsp;|&nbsp; ABOUT US &nbsp;|&nbsp; OUR SERVICES &nbsp;|&nbsp; BLOG &nbsp;|&nbsp; CONTACT</div>
  <div class="copyright">Copyright © 2013 Brindle Harbour Systems ltd. All Rights Reserved.</div>
</footer>

</body>
</html>
```